Vantro #27 - MEN'S NATURAL THERAPEUTIC INTIMATE WASH

Men's Natural Therapeutic INTIMATE Wash
VANTRO #27

Design a 4 oz. stand up tube with flip top cap...
To be packaged in a carton/box

Formula contains Tea Tree OIL
Aloe Vera Gel
Coconut Oil

PRODUCT IS A WASH/SOAP

Helps with
- Jock Itch (tinea cruris)
- Skin Rashes
- Candida
- Itchy Skin

COLORS ON TUBE: Gray, Black, Lime Electric Green and Blue

PRODUCT FOR MEN!

Target Market(s)

MEN

Industry/Entity Type

Retail

Font styles to use
Sans Serif

Colors
9bcb3b
abd036
33a6d7
000000
c9c9c9

Requirements
Must have
• Colors... black, gray, electric green and blue
Nice to have
• Needs to look masculine appeal to the male consumer

```html
<!DOCTYPE html>
<html lang="en">
<head>
<meta charset="utf-8">
<title>Vantro #27 – Men's Natural Therapeutic Intimate Wash</title>
<link href="https://fonts.googleapis.com/css2?family=Jost:wght@400;500;600&display=swap" rel="stylesheet">
<style>
  :root {
    --black: #000000;
    --gray: #c9c9c9;
    --lime: #9bcb3b;
    --lime-bright: #abd036;
    --blue: #33a6d7;
    --white: #ffffff;
    --ink: #1a1a1a;
  }
  * { margin: 0; padding: 0; box-sizing: border-box; }
  html, body {
    width: 1200px; height: 879px; overflow: hidden;
    background: var(--gray);
    font-family: "Jost", sans-serif;
  }
  .tube-label {
    position: absolute; left: 296px; top: 0;
    width: 608px; height: 879px;
    background: var(--black);
    overflow: hidden;
  }
  .brand-name {
    position: absolute; left: 34px; top: 52px;
    font-size: 78px; line-height: 1; font-weight: 500;
    letter-spacing: 2px; color: var(--gray); white-space: nowrap;
  }
  .product-name {
    position: absolute; left: 234px; top: 201px;
    width: 374px; height: 88px;
    background: var(--lime-bright);
    padding: 12px 0 0 18px; color: var(--ink);
  }
  .product-name .tagline { font-size: 20px; font-weight: 500; display: block; }
  .product-name .intimate { font-size: 32px; font-weight: 500; letter-spacing: 1px; }
  .product-name .wash { font-size: 21px; font-weight: 500; }
  .stripe { position: absolute; right: 0; }
  .stripe-lime { left: 255px; top: 322px; height: 9px; background: var(--lime); }
  .stripe-blue { left: 272px; top: 338px; height: 7px; background: var(--blue); }
  .benefits {
    position: absolute; left: 290px; top: 360px;
    width: 318px; height: 161px;
    background: var(--blue); color: var(--white);
    padding: 16px 0 0 22px;
  }
  .benefits h2 { font-size: 19px; font-weight: 500; letter-spacing: 0.5px; margin-bottom: 6px; }
  .benefits ul { list-style: none; font-size: 19px; line-height: 1.2; }
  .ingredients-title {
    position: absolute; left: 292px; top: 778px;
    font-size: 22px; font-weight: 400; letter-spacing: 3px; color: var(--gray);
    white-space: nowrap;
  }
  .rule-white { position: absolute; left: 180px; right: 0; top: 806px; height: 3px; background: var(--white); }
  .ingredients {
    position: absolute; left: 196px; right: 0; top: 812px;
    font-size: 16px; color: var(--white); white-space: nowrap;
  }
  .ingredients span { margin-right: 18px; }
  .ingredients span::before { content: "•"; margin-right: 6px; font-size: 14px; }
  .band-white { position: absolute; left: 0; right: 0; background: var(--white); }
  .band-one { top: 840px; height: 7px; }
  .band-two { top: 858px; height: 9px; }
</style>
</head>
<body>
  <main class="tube-label">
    <div class="brand-name">VANTRO #27</div>

    <div class="product-name">
      <span class="tagline">Men's Natural Therapeutic</span>
      <span class="intimate">INTIMATE</span> <span class="wash">Wash</span>
    </div>

    <div class="stripe stripe-lime"></div>
    <div class="stripe stripe-blue"></div>

    <section class="benefits">
      <h2>HELP WITH</h2>
      <ul>
        <li>- Jock Itch (tinea cruris)</li>
        <li>- Skin Rashes</li>
        <li>- Candida</li>
        <li>- Itchy Skin</li>
      </ul>
    </section>

    <div class="ingredients-title">FORMULA CONTAINS</div>
    <div class="rule-white"></div>
    <div class="ingredients">
      <span>Coconut Oil</span><span>Tea Tree Oil</span><span>Aloe Vera Gel</span>
    </div>

    <div class="band-white band-one"></div>
    <div class="band-white band-two"></div>
  </main>
</body>
</html>
```